Welding Fabrication and Inspection Business Card Design

Welding Fabrication and Inspection Services,

Business

Industrial Machinery ServicesMohammed Rahim30 Ballarat Street, Mount Gravatt East.4122.QLD

```html
<!DOCTYPE html>
<html lang="en">
<head>
<meta charset="utf-8">
<title>Tarnwell Forge Services – Business Card</title>
<link rel="stylesheet" href="https://fonts.googleapis.com/css2?family=Ubuntu:wght@400;500;700&display=swap">
<style>
  :root {
    --backdrop: #e9e6e1;
    --card-dark: #2b2c2f;
    --card-dark-deep: #17181a;
    --mesh-tone: #343539;
    --warm-glow: #4a3b2e;
    --band-white: #ffffff;
    --silver-light: #f4f4f4;
    --silver-mid: #b3b5b7;
    --silver-dark: #6d6f72;
    --ink: #222326;
    --ink-soft: #3c3d40;
    --accent: #f28a22;
    --address: #f4f4f4;
  }
  * { margin: 0; padding: 0; box-sizing: border-box; }
  html, body { width: 1200px; height: 900px; overflow: hidden; }
  body {
    background: var(--backdrop);
    font-family: "Ubuntu", sans-serif;
    display: flex; align-items: center; justify-content: center;
  }
  .business-card {
    position: relative;
    width: 1050px; height: 600px;
    border-radius: 14px;
    overflow: hidden;
    background: var(--card-dark-deep);
    box-shadow: 0 18px 40px rgba(0,0,0,0.25);
  }
  .mesh-panel {
    position: absolute; left: 0; right: 0;
    background: linear-gradient(160deg, var(--mesh-tone) 0%, var(--card-dark) 50%, var(--card-dark-deep) 100%);
  }
  .mesh-panel.top { top: 0; height: 190px; }
  .mesh-panel.bottom { bottom: 0; height: 190px; }
  .spark-area {
    position: absolute; left: 540px; top: 30px;
    width: 200px; height: 130px; border-radius: 10px;
    background: linear-gradient(180deg, var(--card-dark) 0%, var(--warm-glow) 100%);
  }
  .info-band {
    position: absolute; left: 0; right: 0; top: 190px; height: 220px;
    background: var(--band-white);
    border-top: 14px solid var(--silver-mid);
    border-bottom: 14px solid var(--silver-mid);
    box-shadow: inset 0 6px 0 var(--silver-light), inset 0 -6px 0 var(--silver-light);
    display: flex; align-items: center;
  }
  .info-band::before, .info-band::after {
    content: ""; position: absolute; left: 0; right: 0; height: 3px;
    background: linear-gradient(90deg, var(--silver-dark), var(--silver-light), var(--silver-dark));
  }
  .info-band::before { top: -17px; }
  .info-band::after { bottom: -17px; }
  .brand {
    width: 600px; padding-left: 90px;
    display: flex; align-items: center; gap: 16px;
  }
  .brand-mark {
    width: 20px; height: 20px; border-radius: 50%;
    background: var(--ink); flex: none;
  }
  .brand-name {
    font-weight: 700; font-size: 32px; color: var(--ink); white-space: nowrap;
  }
  .divider {
    width: 2px; height: 130px; background: var(--ink-soft); flex: none;
  }
  .contact { padding-left: 42px; color: var(--ink); }
  .person-name { font-weight: 700; font-size: 30px; }
  .person-role { font-size: 21px; margin: 2px 0 12px; color: var(--ink-soft); }
  .contact-line {
    display: flex; align-items: center; gap: 10px;
    font-size: 21px; line-height: 1.5; white-space: nowrap;
  }
  .contact-icon { width: 20px; height: 20px; flex: none; }
  .address {
    position: absolute; left: 0; right: 0; top: 440px;
    text-align: center; padding-left: 260px;
    color: var(--address); font-weight: 500; font-size: 26px; line-height: 1.35;
  }
</style>
</head>
<body>
  <article class="business-card">
    <div class="mesh-panel top" role="img" aria-label="Dark hexagonal mesh texture"></div>
    <div class="spark-area" role="img" aria-label="Welding sparks artwork"></div>
    <div class="mesh-panel bottom" role="img" aria-label="Dark hexagonal mesh texture"></div>

    <section class="info-band">
      <div class="brand">
        <span class="brand-mark"></span>
        <span class="brand-name">Tarnwell Forge Services</span>
      </div>
      <div class="divider"></div>
      <div class="contact">
        <p class="person-name">Khalid Nasser</p>
        <p class="person-role">Owner</p>
        <p class="contact-line">
          <svg class="contact-icon" viewBox="0 0 20 20" aria-hidden="true">
            <rect width="20" height="20" rx="2" fill="var(--accent)"/>
            <path d="M6 4.5l2 2.2-1.2 1.5a8 8 0 0 0 5 5l1.5-1.2 2.2 2-1.3 1.7C9.5 15.5 4.5 10.5 4.3 5.8z" fill="#fff"/>
          </svg>
          0231-4408-7719
        </p>
        <p class="contact-line">
          <svg class="contact-icon" viewBox="0 0 20 20" aria-hidden="true">
            <rect width="20" height="20" rx="2" fill="var(--accent)"/>
            <rect x="4" y="6" width="12" height="8.5" fill="none" stroke="#fff" stroke-width="1.5"/>
            <path d="M4 6l6 5 6-5" fill="none" stroke="#fff" stroke-width="1.5"/>
          </svg>
          khalid@tarnwellforge.com
        </p>
      </div>
    </section>

    <p class="address">17 Corrowen Street, Halbrook Vale<br>4187 QLD</p>
  </article>
</body>
</html>
```